Email Signature & Gatherly Cover Design – Birchlane Study Centre

I’m looking for a clean, professional email signature and a matching Gatherly cover photo for my tutoring business, Birchlane Study Centre.
The email signature needs to display properly across Outlook and iPhone without the image appearing as an attachment. It should include my logo and contact details and have a friendly but professional look suitable for an education business.
Details to include:
Moira Dunholt
Director & Lead Tutor
Birchlane Study Centre
hello@birchlanestudy.co.uk
www.birchlanestudy.co.uk
01632 418736
The Gatherly cover should match the branding, feel professional and welcoming, and be optimised for desktop and mobile.

```html
<!DOCTYPE html>
<html lang="en">
<head>
<meta charset="utf-8">
<title>Birchlane Study Centre – Email Signature</title>
<link rel="stylesheet" href="https://fonts.googleapis.com/css2?family=Raleway:wght@500;600;700&family=Roboto:wght@500&display=swap">
<style>
  :root {
    --brand-green: #41b86a;
    --ink: #333333;
    --ink-soft: #3d3d3d;
    --rule: #e6e6e6;
    --divider: #dcdcdc;
    --card: #ffffff;
    --backdrop: #efeeec;
  }
  * { margin: 0; padding: 0; box-sizing: border-box; }
  html, body {
    width: 1200px; height: 1200px; overflow: hidden;
    background: var(--backdrop);
  }
  .signature {
    position: absolute;
    left: 102px; top: 384px;
    width: 1030px; height: 492px;
    background: var(--card);
    font-family: "Raleway", sans-serif;
    color: var(--ink);
  }
  .brand-name {
    position: absolute;
    left: 40px; top: 96px; width: 270px;
    font-family: "Raleway", sans-serif;
    font-weight: 700;
    color: var(--brand-green);
    font-size: 50px;
    line-height: 1.05;
  }
  .column-divider {
    position: absolute;
    left: 351px; top: 47px;
    width: 1px; height: 299px;
    background: var(--divider);
  }
  .person {
    position: absolute;
    left: 386px; top: 56px;
    white-space: nowrap;
  }
  .person-name {
    font-family: "Roboto", sans-serif;
    font-weight: 500;
    font-size: 30px;
    color: var(--brand-green);
    margin-right: 10px;
  }
  .person-role {
    font-family: "Raleway", sans-serif;
    font-weight: 600;
    font-size: 22px;
    color: var(--ink);
  }
  .rule {
    position: absolute;
    height: 1px;
    background: var(--rule);
  }
  .rule-top { left: 386px; top: 115px; width: 520px; }
  .rule-mid { left: 386px; top: 278px; width: 520px; }
  .rule-foot { left: 39px; top: 384px; width: 952px; }
  .contact-line {
    position: absolute;
    left: 386px;
    font-size: 19px;
    font-weight: 600;
    display: flex; align-items: center;
    height: 26px;
  }
  .contact-label {
    width: 33px;
    color: var(--brand-green);
    font-weight: 500;
  }
  .contact-phone { top: 137px; }
  .contact-email { top: 182px; }
  .contact-web { top: 227px; }
  .social-list {
    position: absolute;
    left: 386px; top: 302px;
    height: 30px;
  }
  .social-item {
    position: absolute;
    top: 0;
    display: flex; align-items: center;
    white-space: nowrap;
    font-size: 17px;
    font-weight: 600;
  }
  .social-dot {
    width: 30px; height: 30px;
    border: 1.5px solid var(--brand-green);
    border-radius: 50%;
    margin-right: 7px;
  }
  .social-sep {
    position: absolute;
    top: 4px;
    width: 1px; height: 24px;
    background: var(--divider);
  }
  .tagline {
    position: absolute;
    left: 39px; top: 418px;
    font-size: 23.5px;
    font-weight: 600;
    letter-spacing: 1.9px;
    color: var(--ink-soft);
    white-space: nowrap;
  }
</style>
</head>
<body>
  <section class="signature">
    <div class="brand-name">Birchlane Study Centre</div>
    <div class="column-divider"></div>

    <div class="person">
      <span class="person-name">Moira Dunholt,</span>
      <span class="person-role">Director &amp; Lead Tutor</span>
    </div>
    <div class="rule rule-top"></div>

    <div class="contact-line contact-phone"><span class="contact-label">M:</span>01632 418736</div>
    <div class="contact-line contact-email"><span class="contact-label">E:</span>hello@birchlanestudy.co.uk</div>
    <div class="contact-line contact-web"><span class="contact-label">W:</span>www.birchlanestudy.co.uk</div>

    <div class="rule rule-mid"></div>

    <div class="social-list">
      <div class="social-item" style="left:0"><span class="social-dot"></span>Circles</div>
      <div class="social-sep" style="left:131px"></div>
      <div class="social-item" style="left:145px"><span class="social-dot"></span>Workline</div>
      <div class="social-sep" style="left:281px"></div>
      <div class="social-item" style="left:305px"><span class="social-dot"></span>Gatherly</div>
      <div class="social-sep" style="left:433px"></div>
      <div class="social-item" style="left:456px"><span class="social-dot"></span>Snapframe</div>
    </div>

    <div class="rule rule-foot"></div>
    <p class="tagline">Where Lessons Land, Curiosity Grows, And Every Step Gets A Smile.</p>
  </section>
</body>
</html>
```